Anhängergestaltung zu einem herausgegebenen Buch
Zielgruppe
Ich habe das Buch 'Wolkenbruch im Garten- Ein Mann bleibt stehen' herausgegeben und möchte, dass das Cover zu ca 50-70 % auf der Fläche erscheint.
Es ist eine passive Werbung.
Wer ich bin oder sein möchte, ergibt sich aus meiner Website, meinem Instagram-Account.
Aufgabenstellung
Ich möchte eine creative Gestaltung mit meinem Buch und Logo auf einer Anhänger-Seite mit H2,05 und Breite 4,00 m. Der weiße Anhänger wird foliert. Linke Seite von der Heckklappe aus. Modell KORVAN T3982 LM.
Das Ganze ist für mich, also damit es mich erfreut. Natürlich auch Werbung für mein Buch, ganz klar. Und nur einfach Vorder- und Rückseite des Buches abzubilden, ist zu einfach.
Für die rechte Seite schreibe ich einen seperaten Pitch aus.
Falls noch creative Idee übrig ist, so als P.S., auf der Seite 2,00 x2,05 wäre eine runde Zielscheibe mit ein paar Insekten, Vögeln, wie auf einer Windschutzschebe nett, also platt, aber wunderschön platt ;)
Sichtbar eher etwas über dem Zugfahrzeug. Aber dieser Teil ist sekundär, kein 'Must-have', sondern ein 'Give-away'.
Ich werde die Daten für das Buchcover hochladen, aber vermutlich zu wenige Pixel. War schließlich für einen anderen Zweck konzipiert.
Und ob ich beim Logo auf Anhieb die richtigen, sprich verwertbaren Daten erwische, ist auch eher zweifelhaft.

```html
<!DOCTYPE html>
<html lang="de">
<head>
<meta charset="utf-8">
<title>Anhängerseite – Wolkenbruch im Garten</title>
<link rel="stylesheet" href="https://fonts.googleapis.com/css2?family=Josefin+Sans:wght@600&family=Libre+Baskerville&display=swap">
<style>
  :root {
    --page-bg: #e9ecef;
    --panel-white: #ffffff;
    --sky-dark: #2f3d5c;
    --sky-mid: #5b6f94;
    --sky-light: #b9c3d3;
    --field-green: #7e8a5e;
    --path-grey: #a9a9a2;
    --poppy-red: #d9321f;
    --poppy-magenta: #9b2a72;
    --cover-text: #ffffff;
    --brand-red: #9e1b24;
    --body-text: #111111;
    --edge: #c9ced4;
  }
  * { margin: 0; padding: 0; box-sizing: border-box; }
  html, body {
    width: 1200px;
    height: 848px;
    overflow: hidden;
    background: var(--page-bg);
  }
  .trailer-side {
    position: absolute;
    left: 40px;
    top: 137px;
    width: 1120px;
    height: 574px;
    background: var(--panel-white);
    border: 1px solid var(--edge);
    display: flex;
  }
  .book-cover {
    position: relative;
    width: 540px;
    height: 100%;
    overflow: hidden;
  }
  .cover-image {
    position: absolute;
    inset: 0;
    background: linear-gradient(180deg,
      var(--sky-dark) 0%,
      var(--sky-mid) 30%,
      var(--sky-light) 50%,
      var(--field-green) 56%,
      var(--path-grey) 72%,
      var(--poppy-red) 86%,
      var(--poppy-magenta) 100%);
  }
  .cover-text {
    position: relative;
    text-align: center;
    color: var(--cover-text);
    font-family: "Libre Baskerville", serif;
    padding-top: 58px;
  }
  .cover-author {
    font-size: 26px;
    letter-spacing: 1px;
  }
  .cover-title {
    margin-top: 34px;
    font-size: 42px;
    font-weight: 400;
    line-height: 1.05;
    letter-spacing: 0.5px;
  }
  .cover-title .small { font-size: 40px; }
  .cover-subtitle {
    margin-top: 14px;
    font-size: 16px;
    letter-spacing: 0.5px;
  }
  .pitch {
    flex: 1;
    display: flex;
    flex-direction: column;
    align-items: center;
    padding-top: 112px;
  }
  .brand-name {
    display: flex;
    align-items: center;
    gap: 12px;
    font-family: "Josefin Sans", sans-serif;
    font-weight: 600;
    font-size: 30px;
    color: var(--brand-red);
    letter-spacing: 1px;
  }
  .brand-name .dot {
    width: 16px;
    height: 16px;
    border-radius: 50%;
    background: var(--brand-red);
  }
  .pitch-text {
    margin-top: 58px;
    font-family: "Josefin Sans", sans-serif;
    font-weight: 600;
    font-size: 28px;
    line-height: 1.42;
    color: var(--body-text);
    text-align: center;
    letter-spacing: 0.5px;
  }
</style>
</head>
<body>
  <main class="trailer-side">
    <section class="book-cover">
      <div class="cover-image" role="img" aria-label="Coverfoto: wolkiger Himmel über weitem Feld, ein Mann mit Schirm und Koffer auf einem Feldweg, davor ein Holzzaun mit roten und violetten Mohnblumen"></div>
      <div class="cover-text">
        <p class="cover-author">Mira Hollbach</p>
        <h1 class="cover-title">WOLKENBRUCH<br><span class="small">im GARTEN</span></h1>
        <p class="cover-subtitle">Ein Mann bleibt stehen</p>
      </div>
    </section>
    <section class="pitch">
      <div class="brand-name"><span class="dot"></span>Mira Hollbach</div>
      <p class="pitch-text">LOREM IPSUM DOLOR SIT<br>AMET, CONSECTETUR ADIP-<br>ISCING ELIT, SED DO EIUS-<br>MOD TEMPOR INCIDIDUNT<br>UT LABORE ET DOLORE<br>MAGNA ALIQUA.</p>
    </section>
  </main>
</body>
</html>
```